Christian Camp Meetings Website Design

**Do not contact me privately; all inquiries will be ignored.**

Industry: Nonprofit Christian camp meetings for children, youth, and adults.

Target Market: Families and individuals seeking a faith-based camp experience.

Description:
This website should provide a visually appealing and easy-to-navigate platform that clearly highlights how visitors can register for camp events and make donations. A straightforward design will make it simple for users to access registration forms, donation buttons, and key event & camp details.

Look and Feel:
• Clean, user-friendly layout focused on clarity and accessibility.
• Primarily blue tones to evoke a calm and welcoming atmosphere.
• Clear, readable Google fonts only.
• If using images only use royalty-free stock photos showcasing participants at camp activities, encouraging new registrations and donations.

Pages to Create:
1. Main Page: A welcoming overview that prominently features call-to-action buttons for registration and donations.
2. Christian Camp Meetings Page: Detailed event information with links to registration forms and suggested donation amounts.
3. Youth Program Page: Descriptions of youth events, programs, and an easy-to-find registration link.
4. Children’s Camp Page: Information about the children’s Bible camp, with a focus on how parents can register their kids.
5. History Page: A brief look at the organization’s origins, with an integrated “Donate Now” button to support ongoing programs.

Examples of Desired Style:
• https://www.brightharborfellowship.org/nrv/
• https://walkingopenroad.com/
• https://www.pinemeadowchapel.org/
• https://kv.church/

Content Source:
Use content from the link provided in the attachment here as the primary source for all textual and media content.

Important Notes:
• Do not contact me privately; all inquiries will be ignored.
• The website should emphasize registration and donations as key actions.
• Avoid overlapping elements in the design; maintain a clean and structured layout.
• Ensure that only Google fonts and royalty-free stock photos are used.

Target Market(s)

Christian families looking for events

Industry/Entity Type

Christian faith based camp

Number of Pages Required

5+ page

Colors
0094D4
00A9DD
6FCCEA
C7EBF8
E9F6FB

Requirements
Should not have
• No search bar, limited or no overlapping elements

```html
<!DOCTYPE html>
<html lang="en">
<head>
<meta charset="utf-8">
<title>Shiloh Grove Camp Association</title>
<link rel="stylesheet" href="https://fonts.googleapis.com/css2?family=Libre+Baskerville:wght@400;700&family=Lato:wght@400;700&display=swap">
<style>
:root{
  --yellow:#f9b914;
  --blue:#0094d4;
  --blue-2:#00a9dd;
  --ink:#1b1b1b;
  --text:#333;
  --green-soft:#dfeec2;
  --footer:#0b0b0b;
  --white:#fff;
}
*{box-sizing:border-box;margin:0;padding:0}
html,body{width:1200px;height:4175px;overflow:hidden}
body{font-family:"Lato",sans-serif;color:var(--text);background:var(--white);position:relative}
.abs{position:absolute}
a{color:inherit;text-decoration:none}

/* header */
.topbar{position:absolute;top:0;left:0;width:1200px;height:103px;background:var(--white)}
.btn-donate-top{position:absolute;left:111px;top:27px;width:160px;height:46px;background:var(--blue);color:#fff;border-radius:5px;font:700 13px "Libre Baskerville",serif;display:flex;align-items:center;justify-content:center;gap:9px;letter-spacing:.5px}
.btn-register{position:absolute;left:917px;top:27px;width:172px;height:46px;border:1.5px solid var(--blue);color:var(--blue);border-radius:5px;font:400 13px "Libre Baskerville",serif;display:flex;align-items:center;justify-content:center;gap:8px}
.navbar{position:absolute;top:103px;left:0;width:1200px;height:65px;background:var(--yellow)}
.navbar a{position:absolute;top:25px;font:700 12px "Libre Baskerville",serif;color:var(--ink);white-space:nowrap}
.brand-badge{position:absolute;left:440px;top:-100px;width:320px;height:195px;border-radius:0 0 160px 160px;background:var(--white);box-shadow:0 0 0 10px rgba(255,255,255,.45);z-index:5;text-align:center}
.brand-badge .name{position:absolute;top:106px;width:100%;font:400 23px "Libre Baskerville",serif;color:var(--ink)}
.brand-badge .sub{position:absolute;top:138px;width:100%;font:400 16px "Lato",sans-serif;letter-spacing:1.5px;color:var(--ink)}
.brand-badge .dot{position:absolute;left:142px;top:40px;width:36px;height:36px;border-radius:50%;background:var(--yellow)}

/* hero */
.hero{position:absolute;top:168px;left:0;width:1200px;height:612px;background:linear-gradient(160deg,#3f5a2b 0%,#6b7a4a 35%,#8c7a5e 60%,#4a3a2c 100%)}
.hero-text{position:absolute;top:128px;width:1200px;text-align:center;color:#fff}
.hero-text .kick{font:700 28px "Libre Baskerville",serif;letter-spacing:1px}
.hero-text h1{font:700 74px "Libre Baskerville",serif;margin-top:14px;letter-spacing:2px}
.btn-yellow{display:flex;align-items:center;justify-content:center;background:var(--yellow);color:var(--ink);border-radius:32px;font:400 19px "Libre Baskerville",serif}
.hero .btn-yellow{position:absolute;left:502px;top:280px;width:196px;height:62px;border:2px solid #fff}

/* camp meetings */
.camp{position:absolute;top:700px;left:0;width:1200px;height:771px;background:linear-gradient(180deg,#d4e8a8 0%,#e9f3d4 45%,#fff 100%)}
.section-mark{width:30px;height:30px;border-radius:50%;background:var(--yellow);margin:0 auto}
.section-title{font:400 44px "Libre Baskerville",serif;color:var(--ink);text-align:center;letter-spacing:1px}
.card{position:absolute;top:236px;width:290px;height:326px;background:#fff;border-radius:6px;box-shadow:0 3px 10px rgba(0,0,0,.12);overflow:hidden;text-align:center}
.card-head{height:100px;background:var(--yellow);display:flex;align-items:center;justify-content:center;font:400 19px/34px "Libre Baskerville",serif;color:var(--ink);padding:0 20px}
.card-body{padding:22px 24px 0;font-size:15px;line-height:29px;color:#333}
.card-body p.small{font-size:13.5px;line-height:27px;margin-top:4px}
.camp .btn-yellow{position:absolute;left:517px;top:622px;width:166px;height:60px}

/* about */
.about{position:absolute;top:1471px;left:0;width:1200px;height:591px}
.about-photo{position:absolute;left:0;top:0;width:600px;height:591px;background:linear-gradient(135deg,#b98a78 0%,#e6dcd4 45%,#8a6150 100%)}
.about-panel{position:absolute;left:600px;top:0;width:600px;height:591px;background:var(--blue);color:#fff;padding:66px 100px 0 86px}
.about-panel h2{font:400 46px "Libre Baskerville",serif;margin-top:24px}
.about-panel p{font-size:14.5px;line-height:26px;margin-top:18px}
.btn-white{position:absolute;left:86px;top:473px;width:198px;height:62px;border-radius:32px;background:#fff;color:var(--ink);font:400 19px "Libre Baskerville",serif;display:flex;align-items:center;justify-content:center}

/* youth */
.youth{position:absolute;top:2062px;left:0;width:1200px;height:680px}
.y-card{position:absolute;top:236px;width:318px}
.y-photo{height:202px;position:relative}
.y-date{position:absolute;left:12px;top:12px;width:50px;height:50px;background:var(--yellow);text-align:center;color:var(--ink);font:700 17px/24px "Lato",sans-serif;padding-top:3px}
.y-date span{display:block;font:400 10px/12px "Lato",sans-serif}
.y-card h3{font:400 18.5px "Libre Baskerville",serif;color:var(--ink);margin-top:16px}
.y-card p{font-size:13.5px;line-height:23px;color:#555;margin-top:6px}
.y-card a{display:inline-block;margin-top:14px;margin-left:2px;font:400 12px "Libre Baskerville",serif;color:#666;text-decoration:underline;letter-spacing:.5px}

/* children */
.kids-photo{position:absolute;top:2742px;left:0;width:1200px;height:590px;background:linear-gradient(100deg,#4c5a57 0%,#b88a66 35%,#c9714a 55%,#e4dcd3 100%)}
.kids-panel{position:absolute;top:3237px;left:136px;width:926px;height:537px;background:#fff;text-align:center;padding-top:38px}
.kids-panel .section-title{font-size:48px;margin-top:32px}
.kids-panel p{font-size:14.5px;line-height:28px;color:#333;padding:0 54px;margin-top:16px}
.kids-panel .btn-yellow{position:absolute;left:381px;top:396px;width:166px;height:60px}

/* footer */
.footer{position:absolute;top:3774px;left:0;width:1200px;height:401px;background:var(--footer);color:#fff}
.f-logo{position:absolute;left:129px;top:64px;width:216px;height:216px;border-radius:50%;border:12px solid #555;background:#fff;text-align:center;color:var(--ink)}
.f-logo .name{margin-top:80px;font:400 16px "Libre Baskerville",serif}
.f-logo .sub{font-size:11px;letter-spacing:1px;margin-top:2px}
.f-col{position:absolute;top:74px}
.f-col h4{font:400 19px "Libre Baskerville",serif;letter-spacing:.5px}
.f-col li{list-style:none;font-size:14.5px;margin-top:17px;padding-left:6px}
.f-contact{position:absolute;left:873px;top:74px}
.f-contact h4{font:400 19px "Libre Baskerville",serif;letter-spacing:.5px}
.f-row{display:flex;align-items:flex-start;gap:14px;font-size:14.5px;line-height:26px}
.f-icon{width:30px;height:30px;border-radius:50%;background:#fff;display:flex;align-items:center;justify-content:center;flex:none}
.f-rule{position:absolute;left:111px;top:325px;width:977px;height:1px;background:#666}
.f-copy{position:absolute;top:358px;width:1200px;text-align:center;font-size:14.5px}
</style>
</head>
<body>

<header>
  <div class="topbar">
    <a class="btn-donate-top" href="#donate">
      <svg width="14" height="13" viewBox="0 0 24 22"><path d="M12 21 2.5 11.5A5.5 5.5 0 0 1 12 4a5.5 5.5 0 0 1 9.5 7.5Z" fill="#fff"/></svg>DONATE NOW</a>
    <a class="btn-register" href="#register">
      <svg width="16" height="16" viewBox="0 0 24 24" fill="none" stroke="#0094d4" stroke-width="2"><rect x="4" y="3" width="13" height="17" rx="1"/><path d="M8 8h6M8 12h4"/><circle cx="17" cy="17" r="3"/></svg>REGISTER NOW</a>
  </div>
  <nav class="navbar">
    <a style="left:70px" href="#">HOME</a>
    <a style="left:139px" href="#">CHRISTIAN CAMP</a>
    <a style="left:286px" href="#">YOUTH PROGRAM</a>
    <a style="left:787px" href="#">CHILDREN’S CAMP</a>
    <a style="left:943px" href="#">HISTORY</a>
    <a style="left:1035px" href="#">CONTACT US</a>
    <div class="brand-badge">
      <div class="dot"></div>
      <div class="name">SHILOH GROVE</div>
      <div class="sub">CAMP ASSOCIATION</div>
    </div>
  </nav>
</header>

<section class="hero" role="img" aria-label="Campers sitting on the grass with open Bibles, hands folded in prayer">
  <div class="hero-text">
    <div class="kick">WELCOME TO</div>
    <h1>SHILOH GROVE</h1>
  </div>
  <a class="btn-yellow" href="#">GET STARTED</a>
</section>

<section class="camp">
  <svg class="abs" style="left:0;top:0" width="1200" height="80" viewBox="0 0 1200 80" preserveAspectRatio="none"><path d="M0 80 V0 H1200 V80 Q900 0 600 0 Q300 0 0 80Z" fill="#5b6b3a"/><path d="M290 28 Q600 -4 1000 22" stroke="#111" stroke-width="5" fill="none"/></svg>
  <div class="abs" style="top:80px;width:1200px"><div class="section-mark"></div></div>
  <h2 class="section-title abs" style="top:150px;width:1200px">CHRISTIAN CAMP MEETINGS</h2>

  <article class="card" style="left:112px">
    <div class="card-head">Shiloh Bible Camp — June 23-26</div>
    <div class="card-body">
      <p>Chosen 1 Peter 2:9</p>
      <p>Fri, Jun 27, 2025 10:00AM - Sat, Jun 28, 2025 1:30PM CDT</p>
      <p class="small">Join us this year at Shiloh the Beginning for "UNCHARTED 2025." Where we will look at controlling our</p>
    </div>
  </article>
  <article class="card" style="left:455px">
    <div class="card-head">Shiloh Bible Camp — June 23-26</div>
    <div class="card-body">
      <p>Chosen 1 Peter 2:9</p>
      <p>Sun, Jun 15, 2025 4:30PM - Sat, Jun 21, 2025 8:30AM CDT</p>
      <p class="small">We want to invite you to join us at Shiloh Bible Camp. Our theme this year is "Campfire Chronicles-Life with</p>
    </div>
  </article>
  <article class="card" style="left:798px">
    <div class="card-head">Shiloh: the Beginning — June 27-28</div>
    <div class="card-body">
      <p>Chosen 1 Peter 2:9</p>
      <p>Mon, Jun 23, 2025 10:30AM - Thur Jun 26, 2025 4:00PM CDT</p>
      <p class="small">We want to you to join us at Shiloh Youth Instituite for a week of Christian growth and community.</p>
    </div>
  </article>
  <a class="btn-yellow" href="#">DONATE</a>
</section>

<section class="about">
  <div class="about-photo" role="img" aria-label="Hands folded in prayer over an open Bible on a table"></div>
  <div class="about-panel">
    <div class="section-mark" style="margin:0"></div>
    <h2>ABOUT US</h2>
    <p>Come and enjoy our open air tabernacle and our air-conditioned dining hall.We have celebrated over 100 years of holiness preaching and worship and would like to add you to our family.</p>
    <p style="margin-top:24px">Shiloh Grove Camp Meeting is an interdenominational Christian Association established for the purpose of getting sinners saved, backsliders reclaimed, and believers sanctified wholly. When you enter Shiloh Grove Campground in Harlan Springs, Illinois, you are standing on holy ground.</p>
    <a class="btn-white" href="#">READ MORE</a>
  </div>
</section>

<section class="youth">
  <div class="abs" style="top:70px;width:1200px"><div class="section-mark"></div></div>
  <h2 class="section-title abs" style="top:140px;width:1200px">YOUTH PROGRAM</h2>

  <article class="y-card" style="left:92px">
    <div class="y-photo" role="img" aria-label="Two women reading together at a table" style="background:linear-gradient(120deg,#c8c2b8,#6f93a8 50%,#a8b39a)"><div class="y-date">15<span>Jun 24</span></div></div>
    <h3>Youth Camps at Shiloh</h3>
    <p>We want to invite you to join us at Shiloh Youth Institute for a week of Christian growth and community.</p>
    <a href="#">REGISTRATION NOW</a>
  </article>
  <article class="y-card" style="left:441px">
    <div class="y-photo" role="img" aria-label="Campfire burning outdoors at dusk" style="background:linear-gradient(180deg,#6a6a5e,#3a342c 55%,#c0602a 75%,#2a2622)"><div class="y-date">01<span>Aug 25</span></div></div>
    <h3>Shiloh Grove Family Camp 2025</h3>
    <p>Come enjoy our opern air tabernacle and our air conditioned dining hall.</p>
    <a href="#">REGISTRATION NOW</a>
  </article>
  <article class="y-card" style="left:788px">
    <div class="y-photo" role="img" aria-label="Tent on a hillside at sunset" style="background:linear-gradient(160deg,#d8d8d2,#e89a3a 55%,#6a5a3a)"><div class="y-date">15<span>Jun 24</span></div></div>
    <h3>Shiloh the Beginning 2025</h3>
    <p>Join us this year at Shiloh the Beginning for "UNCHARTED 2025." Where we will look at controlling our uncharted emotions with God's help!</p>
    <a href="#">REGISTRATION NOW</a>
  </article>
</section>

<div class="kids-photo" role="img" aria-label="Young girl holding hands in prayer at a family table"></div>
<section class="kids-panel">
  <div class="section-mark"></div>
  <h2 class="section-title">CHILDREN’S CAMP</h2>
  <p>Shiloh Grove Camp Meeting is an interdenominational Christian Association established for the purpose of getting sinners saved, backsliders reclaimed, and believers sanctified wholly. It is especially established for preaching the Wesleyan doctrine of baptism of the Holy Spirit (i.e. sanctification, Christian Perfection, holiness) as a second definite work of God’s grace in the human heart.</p>
  <p style="margin-top:26px">When you enter Shiloh Grove Campground in Harlan Springs, Illinois, you are standing on holy ground.</p>
  <a class="btn-yellow" href="#">DONATE</a>
</section>

<footer class="footer">
  <div class="f-logo">
    <div class="name">SHILOH GROVE</div>
    <div class="sub">CAMP ASSOCIATION</div>
  </div>
  <div class="f-col" style="left:430px">
    <h4>QUICK LINKS</h4>
    <ul><li>Home</li><li>Christian Camp Meeting</li><li>Youth Program</li><li>Children’s Camp</li><li>Contact Us</li></ul>
  </div>
  <div class="f-col" style="left:678px">
    <h4>HELP LINKS</h4>
    <ul><li>FAQ</li><li>Terms of use</li><li>Privacy Policy</li><li>Support Links</li><li>Conditions</li></ul>
  </div>
  <div class="f-contact">
    <h4>CONTACT US</h4>
    <div class="f-row" style="margin-top:18px">
      <span class="f-icon"><svg width="14" height="16" viewBox="0 0 24 24"><path d="M12 2a7 7 0 0 0-7 7c0 5 7 13 7 13s7-8 7-13a7 7 0 0 0-7-7Zm0 10a3 3 0 1 1 0-6 3 3 0 0 1 0 6Z" fill="#000"/></svg></span>
      <span>412 Meadowlark Lane<br>Harlan Springs, IL 62930</span>
    </div>
    <div class="f-row" style="margin-top:14px;align-items:center">
      <span class="f-icon"><svg width="14" height="14" viewBox="0 0 24 24"><path d="M6.6 10.8a15 15 0 0 0 6.6 6.6l2.2-2.2c.3-.3.7-.4 1-.2 1.1.4 2.3.6 3.6.6.6 0 1 .4 1 1V20c0 .6-.4 1-1 1A17 17 0 0 1 3 4c0-.6.4-1 1-1h3.5c.6 0 1 .4 1 1 0 1.3.2 2.5.6 3.6.1.3 0 .7-.2 1Z" fill="#000"/></svg></span>
      <span>618-555-0142</span>
    </div>
    <div class="f-row" style="margin-top:22px;align-items:center">
      <span class="f-icon"><svg width="14" height="12" viewBox="0 0 24 20"><rect x="1" y="2" width="22" height="16" rx="2" fill="#000"/><path d="M2 4l10 7 10-7" stroke="#fff" stroke-width="2" fill="none"/></svg></span>
      <span>info@shilohgrove.org</span>
    </div>
  </div>
  <div class="f-rule"></div>
  <div class="f-copy">Copyrights@2025.Shiloh Grove.All Rights Reserved</div>
</footer>

</body>
</html>
```